Pebble Lantern Fine Chocolates
Handcrafted in Tucson, Arizona
tolquartdraws: would you like to try stationary to go with #29?? I like all the dripping chocolate :) Maybe also make the logo slightly bigger and remove the little icons in front of contact info?? Thanks!!
Oh, and I guess you would not have to text Tucson, Arizona since that is already in the Logo.
I am really am liking all these variations. I'm not sure I like the little icons in front of name, phone, email, web address, etc. I would like it to be clear and easy to read quickly, also artistic. Thanks for all your submissions!!

```html
<!DOCTYPE html>
<html lang="en">
<head>
<meta charset="utf-8">
<title>Pebble Lantern Fine Chocolates – Business Card</title>
<link rel="stylesheet" href="https://fonts.googleapis.com/css2?family=Lora:ital,wght@0,700;1,700&family=Arimo:wght@400&display=swap">
<style>
  :root {
    --page-bg: #e9e4dc;
    --card-bg: #ffffff;
    --brand-red: #7d1414;
    --tab-red: #a3161b;
    --ink: #1e1e1e;
    --ink-soft: #3a3a3a;
    --divider: #c9c9c9;
    --logo-disc: #f6f0c8;
  }
  html, body {
    margin: 0;
    width: 1200px;
    height: 965px;
    overflow: hidden;
    background: var(--page-bg);
  }
  .business-card {
    position: absolute;
    left: 110px;
    top: 205px;
    width: 980px;
    height: 555px;
    background: var(--card-bg);
    border-radius: 36px;
    box-shadow: 0 10px 28px rgba(0,0,0,0.22);
  }
  .edge-tab {
    position: absolute;
    right: 0;
    top: 180px;
    width: 22px;
    height: 180px;
    background: var(--tab-red);
    border-radius: 8px 0 0 8px;
  }
  .brand-block {
    position: absolute;
    left: 30px;
    top: 82px;
    width: 376px;
    height: 373px;
    display: flex;
    flex-direction: column;
    align-items: center;
    justify-content: center;
    gap: 22px;
  }
  .brand-disc {
    width: 124px;
    height: 124px;
    border-radius: 50%;
    background: var(--logo-disc);
  }
  .brand-name {
    margin: 0;
    font-family: "Lora", Georgia, serif;
    font-weight: 700;
    font-size: 40px;
    line-height: 1.15;
    color: var(--brand-red);
    text-align: center;
  }
  .divider {
    position: absolute;
    left: 425px;
    top: 100px;
    width: 2px;
    height: 360px;
    background: var(--divider);
  }
  .contact-block {
    position: absolute;
    left: 455px;
    top: 118px;
    font-family: "Arimo", Arial, sans-serif;
  }
  .person-name {
    margin: 0;
    font-family: "Lora", Georgia, serif;
    font-style: italic;
    font-weight: 700;
    font-size: 40px;
    color: var(--brand-red);
    line-height: 1.1;
  }
  .person-title {
    margin: 6px 0 0;
    font-family: "Lora", Georgia, serif;
    font-style: italic;
    font-weight: 700;
    font-size: 26px;
    color: var(--ink);
  }
  .contact-list {
    list-style: none;
    margin: 118px 0 0;
    padding: 0;
  }
  .contact-list li {
    font-size: 23px;
    line-height: 37px;
    color: var(--ink-soft);
  }
</style>
</head>
<body>
  <div class="business-card">
    <div class="edge-tab"></div>

    <div class="brand-block">
      <div class="brand-disc"></div>
      <p class="brand-name">Pebble Lantern<br>Fine Chocolates</p>
    </div>

    <div class="divider"></div>

    <div class="contact-block">
      <h1 class="person-name">Rosalind Okafor</h1>
      <p class="person-title">Chocolatier</p>
      <ul class="contact-list">
        <li>520-555-0147</li>
        <li>rosa@pebblelanternchocolates.com</li>
        <li>pebblelanternchocolates.com</li>
      </ul>
    </div>
  </div>
</body>
</html>
```